Help Liu Wenhao redesign his business card!

Liu Wenhao, an "influential" Chinese businessman, made international headlines this week with his business card...but not for the right reasons. Help Liu Wenhao redesign his new business card - funny and/or satirical submissions welcome!

Check out his hilarious business card that he was giving out on a trip to New York, with not one, not two...but TEN titles! Let's just say they're not the most humble titles either :).

Read more about Liu's business card here: http://blogs.brightledger.example/asiadesk/2014/01/14/liu-wenhaos-business-card-needs-to-be-recycled/

While the rest of the world is laughing at him, we want to help. This is an unofficial contest, but we'd like the PixelForge community to have a shot at redesigning Liu's business card. Thousands of businesses have used PixelForge.example to create beautiful business cards, so we know the community of designers here can do a great job.

We'd like you to create a business card worthy of this honorable businessman, while also keeping a clean, dignified design.

Funny / satirical job titles and designs are encouraged. Note you do not have to use all of Liu's titles on the card. Feel free to come up with your own creative titles!

In regard to contact details, please use dummy contact details. Liu's company name and street address are:

China Tai-Mo Reusable Scrap & Restoration Corporation
Fuxing Road 7, Lanqiao District, Nanjing, China

You can design a single sided or double-sided card - it's completely up to you!

Target Market(s)

Business people and government officials of the world

Industry/Entity Type

Business

Font styles to use
Serif
Sans Serif
Decorative

Colors
ec2027
ffc214
6b449b
0455a3

Requirements
Must have
• At least 1 title, preferably more than 1.

Designers can approach this task how they like however one option could be to use one of Liu's titles and create a suitable business card graphic to suit the role. Designers are also encouraged to o make up a new title and design a graphic to suit.

Here are the titles - but you can also make up your own!

Most influential person of China
Most prominent Philanthropist of China
China Moral Leader
China Earthquake Rescue Hero
Most well-known and Beloved Chinese Role Model
China Top Ten Most Honorable Volunteer
Most Charismatic Philanthropist of China
China Low Carbon Emission
Environmental Protection Top Advocate
China's Foremost Environmental Preservation Demolition Expert
Should not have
• No black borders around photographs of Liu Wenhao
Do not present Liu Wenhao's image in grayscale (black and white)

For a detailed guideline for colors to avoid in design targeting the Chinese market, see http://www.corvalegroup.example/2011/01/17/color/

```html
<!DOCTYPE html>
<html lang="en">
<head>
<meta charset="utf-8">
<title>Liu Wenhao Business Card</title>
<link rel="stylesheet" href="https://fonts.googleapis.com/css2?family=Quicksand:wght@400;700&display=swap">
<style>
  :root {
    --page-bg: #e9e7e3;
    --card-yellow: #ffc233;
    --card-navy: #3e4a86;
    --stripe-white: #ffffff;
    --title-white: #ffffff;
    --company-green: #1ea95a;
    --photo-top: #9ec3df;
    --photo-bottom: #2c2f3a;
  }
  html, body {
    margin: 0;
    padding: 0;
    width: 1200px;
    height: 901px;
    overflow: hidden;
    background: var(--page-bg);
  }
  .canvas {
    position: relative;
    width: 1200px;
    height: 901px;
  }
  .business-card {
    position: absolute;
    left: 100px;
    top: 164px;
    width: 1000px;
    height: 572px;
    border-radius: 22px;
    overflow: hidden;
    background: var(--card-yellow);
    box-shadow: 0 18px 40px rgba(0, 0, 0, 0.18);
  }
  .card-top {
    position: absolute;
    left: 0;
    top: 0;
    width: 100%;
    height: 386px;
    background: var(--card-yellow);
  }
  .portrait {
    position: absolute;
    left: 62px;
    top: 96px;
    width: 190px;
    height: 232px;
    background: linear-gradient(180deg, var(--photo-top) 0%, var(--photo-top) 45%, var(--photo-bottom) 100%);
  }
  .title-list {
    position: absolute;
    left: 292px;
    top: 62px;
    margin: 0;
    padding: 0;
    list-style: none;
    font-family: "Quicksand", sans-serif;
    font-weight: 400;
    font-size: 24px;
    line-height: 30.5px;
    letter-spacing: -0.6px;
    color: var(--title-white);
  }
  .divider-stripe {
    position: absolute;
    left: 0;
    top: 386px;
    width: 100%;
    height: 16px;
    background: var(--stripe-white);
  }
  .card-bottom {
    position: absolute;
    left: 0;
    top: 402px;
    width: 100%;
    height: 170px;
    background: var(--card-navy);
    display: flex;
    flex-direction: column;
    justify-content: center;
    align-items: center;
    font-family: "Quicksand", sans-serif;
    font-weight: 700;
    color: var(--company-green);
    text-transform: uppercase;
    letter-spacing: 2px;
  }
  .company-name,
  .company-address {
    margin: 0;
    font-size: 23px;
    line-height: 34px;
  }
</style>
</head>
<body>
<main class="canvas">
  <article class="business-card">
    <section class="card-top">
      <div class="portrait" role="img" aria-label="Colour portrait photo of Liu Wenhao in a dark suit and tie against a light blue backdrop"></div>
      <ul class="title-list">
        <li>Most influential person of China</li>
        <li>Most prominent Philanthropist of China</li>
        <li>China Moral Leader</li>
        <li>China Earthquake Rescue Hero</li>
        <li>Most well-known and Beloved Chinese Role Model</li>
        <li>China Top Ten Most Honorable Volunteer</li>
        <li>Most Charismatic Philanthropist of China</li>
        <li>China Low Carbon Emission</li>
        <li>Environmental Protection Top Advocate</li>
        <li>China's Foremost Environmental Preservation Demolition Expert</li>
      </ul>
    </section>
    <div class="divider-stripe"></div>
    <footer class="card-bottom">
      <p class="company-name">China Tai-Mo Reusable Scrap &amp; Restoration Corporation</p>
      <p class="company-address">Fuxing Road 7, Lanqiao District, Nanjing, China</p>
    </footer>
  </article>
</main>
</body>
</html>
```